Tilbury Pane Works Business Card

We need a business card design that is suitable for a Glazing Business. We Specialize in Repairing broken windows and doors and are a 24hr on call service. We manufacture Shower screens, Fly screens, Wardrobe doors, Security doors and grilles + mirrors. We stock a variety of mesh including Standard mesh, Pet resistant mesh, Metrashield & Clearvexa. We would like to use a combination of Light Blue, Dark Blue, Black & White with perhaps a picture of glass breaking.

Industry/Entity Type

Business

Contact Information for Business Card

Tilbury Glass Service60B Glasshouse Rocks RdNarooma NSW 2546PH / FAX - 02 44765210MOB - 0418356072 Andrewemail - tilburypane@mailbox-example.net

Font styles to use
Serif

Colors
34a7d8
0255a3
ffffff

Requirements
Must have
• logo with picture of broken or cracked glass

```html
<!DOCTYPE html>
<html lang="en">
<head>
<meta charset="utf-8">
<title>Tilbury Pane Works – Business Card</title>
<link rel="stylesheet" href="https://fonts.googleapis.com/css2?family=Poppins:wght@600&family=Open+Sans:wght@400;600&display=swap">
<style>
  :root {
    --backdrop: #141414;
    --card-top: #5fc9e5;
    --card-bottom: #3a82c8;
    --ink: #ffffff;
  }
  * { margin: 0; padding: 0; box-sizing: border-box; }
  html, body { width: 1200px; height: 900px; overflow: hidden; }
  body {
    background: var(--backdrop);
    position: relative;
    font-family: "Open Sans", sans-serif;
    color: var(--ink);
  }
  .card {
    position: absolute;
    top: 306px;
    width: 439px;
    height: 271px;
    border-radius: 10px;
    background: linear-gradient(180deg, var(--card-top) 0%, var(--card-bottom) 100%);
  }
  .card--front { left: 149px; }
  .card--back { left: 609px; }

  .wordmark {
    position: absolute;
    left: 0; right: 0;
    text-align: center;
    font-family: "Poppins", sans-serif;
    font-weight: 600;
    line-height: 1;
  }
  .wordmark__name { display: block; letter-spacing: 0.04em; }
  .wordmark__trade { display: block; letter-spacing: 0.36em; padding-left: 0.36em; }

  .card--front .wordmark { top: 60px; }
  .card--front .wordmark__name { font-size: 44px; }
  .card--front .wordmark__trade { font-size: 17px; margin-top: 5px; }

  .card--back .wordmark { top: 68px; }
  .card--back .wordmark__name { font-size: 50px; }
  .card--back .wordmark__trade { font-size: 20px; margin-top: 7px; }

  .holder {
    position: absolute;
    right: 242px;
    top: 153px;
    text-align: right;
  }
  .holder__name { font-size: 16px; font-weight: 600; line-height: 20px; }
  .holder__address { font-size: 12px; line-height: 18px; margin-top: 13px; }

  .contacts {
    position: absolute;
    left: 220px;
    top: 152px;
    list-style: none;
    font-size: 12px;
    line-height: 18px;
  }
  .contacts li { display: flex; align-items: center; gap: 7px; }
  .contacts li.email { font-size: 11px; margin-top: 1px; }
  .contacts svg { width: 10px; height: 10px; fill: var(--ink); flex: none; }

  .services {
    position: absolute;
    left: 0; right: 0;
    top: 179px;
    text-align: center;
    font-size: 12.5px;
    font-weight: 600;
    line-height: 20px;
  }
  .services span { white-space: nowrap; }
  .services span::before {
    content: "";
    display: inline-block;
    width: 9px; height: 9px;
    border-radius: 50%;
    background: rgba(255,255,255,0.85);
    margin: 0 4px 0 3px;
    vertical-align: -1px;
  }
</style>
</head>
<body>

<section class="card card--front" aria-label="Business card front">
  <h1 class="wordmark">
    <span class="wordmark__name">TILBURY</span>
    <span class="wordmark__trade">Pane Works</span>
  </h1>

  <div class="holder">
    <p class="holder__name">Graham</p>
    <p class="holder__address">47D Wattlebank Ridge<br>RdTilbury NSW 2583</p>
  </div>

  <ul class="contacts">
    <li>
      <svg viewBox="0 0 10 10" aria-hidden="true"><path d="M2 0.5 L3.6 2.6 L2.8 3.6 Q4 6 6.4 7.2 L7.4 6.4 L9.5 8 L8.5 9.5 Q3.5 9 0.5 1.5 Z"/></svg>
      02 48213967
    </li>
    <li>
      <svg viewBox="0 0 10 10" aria-hidden="true"><path d="M2.5 0.5 H7.5 V3 H9.5 V8.5 H0.5 V3 H2.5 Z M3.5 1.5 V3 H6.5 V1.5 Z M2.5 5.5 V7 H7.5 V5.5 Z"/></svg>
      02 48213967
    </li>
    <li>
      <svg viewBox="0 0 10 10" aria-hidden="true"><path d="M2.5 0 H7.5 V10 H2.5 Z M3.3 1 V7.8 H6.7 V1 Z M4.5 8.4 H5.5 V9.3 H4.5 Z"/></svg>
      0418356072
    </li>
    <li class="email">
      <svg viewBox="0 0 10 10" aria-hidden="true"><path d="M0.5 2 H9.5 V8 H0.5 Z M1.2 2.6 L5 5.4 L8.8 2.6 Z" fill-rule="evenodd"/></svg>
      tilburypane@mailbox-example.net
    </li>
  </ul>
</section>

<section class="card card--back" aria-label="Business card back">
  <h2 class="wordmark">
    <span class="wordmark__name">TILBURY</span>
    <span class="wordmark__trade">Pane Works</span>
  </h2>

  <p class="services">
    <span>Shower screens</span> <span>Fly screens</span> <span>Wardrobe doors</span><br>
    <span>Security doors</span> <span>Grilles + mirrors</span>
  </p>
</section>

</body>
</html>
```